Kitchen and Bathroom Remodeling Flyer

This flyer is for a home remodeling company that remodels peoples kitchens and bathrooms.

We want a flyer to be sophisticated: nice professional design with classy font.

FRONT OF FLYER:

I have attached the front flyer I created and there is no design to it. The reason is so you can see what text elements we want on the flyer. a second attachment has the text for easy copy and paste.

I like the idea of mentioning “Owners live in Ahwatukee” because this flyer will be passed around door to door in that town of Ahwatukee.

Please use the image and the corresponding headline specific to that image. The headline can be in the image or to the top of the image.

BACK OF FLYER:
The back of flyer is essentially a written letter with a profile image of our owners and then two testimonials at bottom. I’d like to add a little bit of design to the back of the flyer. See attachment for pdf of current text and basic structure.

Our brand colors are gray and blue# 0000cc

Our website is https://Kelmbrookrenovating.com

Thank you,
Tobias

Target Market(s)

Mostly woman. Homeowners making 100k+ a year that want to remodel their kitchen or bathroom

Industry/Entity Type

Home Improvement

Font styles to use
Serif
Sans Serif
Decorative

Colors

Designer to choose colors to be used in the design.

Requirements
Must have
• This has to be in photoshop with each element editable (I’ll want to change things down the road)
Nice to have
• Examples that I don’t want copied but so you have a rough idea of some design structure that I like:
• https://flyer.pixelvantyard.com/contest.aspx?id=5190362
• https://flyer.pixelvantyard.com/contest.aspx?id=627053
• https://flyer.pixelvantyard.com/contest.aspx?id=8831475
• https://www.pixelvantyard.com/design/42957018
• https://www.pixelvantyard.com/design/7160243
Should not have
• Nothing silly or too loud. Thank you

```html
<!DOCTYPE html>
<html lang="en">
<head>
<meta charset="utf-8">
<title>Kelmbrook Renovating – Kitchen &amp; Bathroom Flyer</title>
<link href="https://fonts.googleapis.com/css2?family=Fira+Sans:wght@400;500;600;700&family=Open+Sans:wght@400;600;700&family=Libre+Baskerville:wght@400;700&display=swap" rel="stylesheet">
<style>
:root{
  --brand-blue:#2f3f9c;
  --brand-blue-dark:#27358a;
  --accent-green:#1f9a48;
  --text-gray:#4f5154;
  --soft-gray:#ecedef;
  --light-line:#d8dadd;
  --dot-blue:#33b5f0;
  --page-bg:#e6e6e6;
  --white:#ffffff;
}
*{box-sizing:border-box;margin:0;padding:0}
html,body{width:1200px;height:816px;overflow:hidden}
body{background:var(--page-bg);font-family:"Open Sans",sans-serif;color:var(--text-gray);position:relative}
.flyer-page{position:absolute;top:62px;width:534px;height:685px;background:var(--white);overflow:hidden;box-shadow:0 4px 14px rgba(0,0,0,.18)}
.flyer-back{left:54px}
.flyer-front{left:621px}
.abs{position:absolute}

/* ---------- back page ---------- */
.letter{left:31px;top:30px;width:328px}
.letter-greeting{font-family:"Libre Baskerville",serif;color:var(--brand-blue);font-size:14.5px;margin-bottom:18px}
.letter p{font-size:7.3px;line-height:1.38;text-align:justify;margin-bottom:7px}
.ribbon{left:378px;top:0;width:133px;height:318px;background:var(--brand-blue);border-radius:0 0 66px 66px;color:var(--white);text-align:center;padding:24px 8px 0}
.ribbon-lead{font-family:"Fira Sans",sans-serif;font-weight:600;font-size:10.3px;line-height:1.3;margin-bottom:9px}
.ribbon-copy{font-size:8.4px;line-height:1.35;margin:12px 0 10px}
.ribbon-sub{font-family:"Fira Sans",sans-serif;font-size:13px;font-weight:500}
.ribbon-list{font-size:8.6px;line-height:1.4}
.guarantee-seal{left:403px;top:282px;width:82px;height:82px;border-radius:50%;background:var(--accent-green);border:5px solid #c8cbd3}
.owner-card{left:31px;top:282px;width:333px;height:81px;background:var(--soft-gray)}
.owner-names{left:6px;top:4px;font-family:"Fira Sans",sans-serif;font-weight:600;color:var(--brand-blue);font-size:10.5px}
.owner-details{left:6px;top:25px;font-size:7.8px;line-height:1.62}
.owner-details strong{font-weight:600;color:#333}
.owner-photo{left:119px;top:0;width:65px;height:81px;background:linear-gradient(160deg,#3e6fb8,#1f4c93)}
.owner-brand{left:192px;top:28px;display:flex;align-items:center;gap:5px}
.brand-square{width:10px;height:10px;background:var(--brand-blue)}
.brand-name{font-family:"Libre Baskerville",serif;font-size:10.5px;color:var(--brand-blue)}
.photo-strip{top:384px;height:123px}
.photo-bath{left:0;width:148px;background:linear-gradient(135deg,#6e6a66,#cfcac4)}
.photo-kitchen{left:152px;width:163px;background:linear-gradient(160deg,#9a6a3a,#d9b07a 55%,#7a4d27)}
.photo-white-kitchen{left:318px;width:216px;background:linear-gradient(160deg,#e7e8e6,#bfc4c2)}
.call-band{left:0;top:509px;width:534px;height:33px;background:var(--accent-green);color:var(--white);font-family:"Fira Sans",sans-serif;display:flex;justify-content:space-between;align-items:center;padding:0 32px 0 27px}
.call-band-label{font-size:17px;font-weight:500}
.call-band-phone{font-size:19px;font-weight:600}
.review-panel{left:0;top:542px;width:534px;height:143px;background:var(--brand-blue);color:var(--white)}
.review-title{left:28px;top:10px;font-family:"Fira Sans",sans-serif;font-size:14px;font-weight:600}
.site-tab{left:302px;top:5px;width:200px;height:19px;background:var(--white);color:var(--brand-blue);font-family:"Fira Sans",sans-serif;font-weight:600;font-size:10.5px;display:flex;align-items:center;justify-content:center}
.review-photo{top:36px;width:75px;height:76px;background:linear-gradient(160deg,#8a7a6a,#3e3a36)}
.review-text{top:34px;width:128px;font-size:7.2px;line-height:1.52;text-align:justify}
.review-name{top:104px;font-size:7.6px;font-weight:600}
.review-name span{font-weight:400;font-size:6.6px}

/* ---------- front page ---------- */
.front-shapes{left:0;top:0}
.front-photo-fill{left:0;top:0;width:534px;height:685px}
.front-brand{left:30px;top:52px;display:flex;align-items:center;gap:7px}
.front-brand .brand-square{width:14px;height:14px}
.front-brand .brand-name{font-size:15px}
.front-brand-rule{left:30px;top:96px;width:184px;height:1px;background:var(--text-gray)}
.headline{font-family:"Fira Sans",sans-serif;font-weight:600;color:var(--brand-blue);font-size:23.5px;line-height:1.2}
.headline-kitchen{left:30px;top:122px}
.headline-bath{left:30px;top:250px}
.promises{right:36px;top:26px;text-align:right;color:var(--white);width:230px}
.promises-title{font-family:"Libre Baskerville",serif;font-weight:700;font-size:14.5px;line-height:1.15;margin-bottom:10px}
.promises ul{list-style:none}
.promises li{font-size:8.8px;line-height:1.2;margin-bottom:6px;position:relative}
.promises li.dot::after{content:"";position:absolute;right:-9px;top:3px;width:5px;height:5px;border-radius:50%;background:var(--dot-blue)}
.seal{border-radius:50%;background:var(--accent-green);border:4px solid var(--white);color:var(--white);font-family:"Fira Sans",sans-serif;font-weight:600;text-align:center;display:flex;align-items:center;justify-content:center;line-height:1.17}
.seal-owners{left:303px;top:226px;width:124px;height:124px;font-size:16.5px;padding-bottom:28px}
.seal-licensed{left:41px;top:337px;width:114px;height:114px;font-size:16.5px;box-shadow:0 0 0 2px var(--brand-blue)}
.front-phone{left:30px;top:636px;font-family:"Fira Sans",sans-serif;font-weight:700;color:var(--white);font-size:28px;text-shadow:0 2px 4px rgba(0,0,0,.55)}
</style>
</head>
<body>

<!-- Back side: letter and testimonials -->
<section class="flyer-page flyer-back">
  <div class="abs letter">
    <h1 class="letter-greeting">Dear Ahwatukee Homeowners,</h1>
    <p>Everyone wants a dream home they can be proud of. We all want to feel prosperous in life and our home is an extension of ourselves, our style and feeling successful.</p>
    <p>We understand working with a remodeling contractor can be frustrating because they show up late, change the price and make a mess of your home.</p>
    <p>Kelmbrook Renovating is the most organized remodeling company in the valley and we'll create the dream space you'll be proud to show off to your friends, family, &amp; neighbors.</p>
    <p>One of our co-founders Tobias has been through several contractor nightmares and it is the main reason Tobias, Grant and Miles founded Kelmbrook Renovating.</p>
    <p>We are an award-winning home remodeling licensed contractor that is known for showing up on time, being organized, clearly explaining all aspects of the remodel, adhering to project budget and timeline.</p>
    <p>One of our client's said we were the DriveEasy of home remodeling and we think that's a nice comparison. We'll guide you through our 4 step process and there's no haggle, no sales BS and our clients love the experience.</p>
    <p>To a beautiful home you'll love showing off to your neighbors, family &amp; friends,</p>
  </div>

  <aside class="abs ribbon">
    <p class="ribbon-lead">Your Remodeled Dream Space Without Contractor Issues</p>
    <p class="ribbon-lead" style="font-size:11.3px">Need Bathroom and Kitchen Remodeling in the Phoenix Valley?</p>
    <p class="ribbon-copy">Working with a home remodeling contractor can be frustrating because they show up late, change the price and make a mess of your home.</p>
    <p class="ribbon-sub">We specialize in</p>
    <p class="ribbon-list">KITCHEN &amp; BATHROOM<br>remodeling services in Phoenix, Ahwatukee, Chandler, Gilbert, Tempe, Ocotillo, and Scottsdale.</p>
  </aside>
  <div class="abs guarantee-seal" role="img" aria-label="Licensed, bonded and insured guarantee seal"></div>

  <div class="abs owner-card">
    <p class="abs owner-names">Tobias, Miles and Grant</p>
    <p class="abs owner-details">Kelmbrook Renovating<br>ROC# 420917<br><strong>KelmbrookRenovating.com</strong><br><strong>602-555-0148</strong></p>
    <div class="abs owner-photo" role="img" aria-label="Portrait of a company co-founder"></div>
    <div class="abs owner-brand"><span class="brand-square"></span><span class="brand-name">Kelmbrook Renovating</span></div>
  </div>

  <div class="abs photo-strip photo-bath" role="img" aria-label="Remodeled bathroom with double vanity"></div>
  <div class="abs photo-strip photo-kitchen" role="img" aria-label="Remodeled kitchen with wood floors and island"></div>
  <div class="abs photo-strip photo-white-kitchen" role="img" aria-label="Bright white kitchen with marble island"></div>

  <div class="abs call-band">
    <span class="call-band-label">Get Your Free 15 Min Call</span>
    <span class="call-band-phone">(602) 555-0148</span>
  </div>

  <div class="abs review-panel">
    <h2 class="abs review-title">What our clients have to say:</h2>
    <div class="abs site-tab">www.KelmbrookRenovating.com</div>

    <div class="abs review-photo" style="left:27px" role="img" aria-label="Happy client couple"></div>
    <p class="abs review-text" style="left:108px">Miles and his team were easy to work with and their attention to detail was great. Our kitchen looks perfect just how we wanted it and we couldn't be happier. Thank you Kelmbrook Renovating.</p>
    <p class="abs review-name" style="left:108px">Helena &amp; Marco V. <span>Chandler, AZ</span></p>

    <div class="abs review-photo" style="left:293px" role="img" aria-label="Happy client couple outdoors"></div>
    <p class="abs review-text" style="left:377px">Our bathroom is amazing! The crew was polite, easy to work with and they kept our house clean. I always knew what was happening and there weren't any surprises. My wife and I are very happy. Thank you!</p>
    <p class="abs review-name" style="left:377px">Owen &amp; Tess L. <span>Biltmore Phoenix, AZ</span></p>
  </div>
</section>

<!-- Front side: headlines, promises and kitchen scene -->
<section class="flyer-page flyer-front">
  <div class="abs front-photo-fill" role="img" aria-label="Father and daughter baking together in a bright white kitchen" style="background:linear-gradient(170deg,#d9d6cf 0%,#b9b4aa 45%,#6d6a66 100%)"></div>
  <svg class="abs front-shapes" width="534" height="685" viewBox="0 0 534 685" aria-hidden="true">
    <path d="M0,0 H534 V215 C440,240 360,290 290,340 C200,395 90,415 0,420 Z" fill="#ecedef"/>
    <path d="M0,0 H398 C362,100 348,182 302,212 C240,242 120,234 0,238 Z" fill="#ffffff"/>
    <path d="M425,0 H534 V214 C480,232 420,252 372,272 C332,242 326,182 342,130 C360,72 392,30 425,0 Z" fill="#2f3f9c"/>
    <path d="M398,0 C362,100 348,182 302,212 C240,242 120,234 0,238" fill="none" stroke="#2f3f9c" stroke-width="7"/>
    <path d="M0,422 C90,420 200,400 290,343 C360,296 440,244 534,218" fill="none" stroke="#2f3f9c" stroke-width="7"/>
  </svg>

  <div class="abs front-brand"><span class="brand-square"></span><span class="brand-name">Kelmbrook Renovating</span></div>
  <div class="abs front-brand-rule"></div>

  <h1 class="abs headline headline-kitchen">Entertain in a kitchen<br>you'll love showing<br>off to friends &amp; family</h1>
  <h2 class="abs headline headline-bath">Turn an old<br>bathroom into your<br>own personal spa</h2>

  <div class="abs promises">
    <h2 class="promises-title">OUR CLIENT<br>PROMISES</h2>
    <ul>
      <li class="dot">Provide honest and straight<br>forward advice</li>
      <li class="dot">Return calls and show up on time</li>
      <li class="dot">Employ professional, respectful<br>and knowledgeable employees</li>
      <li class="dot">Respect your home and ensure we<br>keep it clean</li>
      <li class="dot">Provide clear expectations of<br>project timelines and pricing</li>
      <li>Create your dream living space with<br>great attention to detail</li>
    </ul>
  </div>

  <div class="abs seal seal-owners">OWNERS<br>LIVE IN<br>AHWATUKEE</div>
  <div class="abs seal seal-licensed">LICENSED<br>BONDED<br>INSURED</div>

  <p class="abs front-phone">(602) 555-0148</p>
</section>

</body>
</html>
```